Letter design, envelope design, and more

Hello, we the Varlo Gmbh are looking for our shop. Letter C5. Design does not have to be like a business card, so it can have straight lines. Only the color is important. The logo is the text under VaRLo omit.It should not be playful but Profesionel

Font styles to use
Sans Serif

Colors
0555a3
3176b5
85abd2
85cae6
34a7d8
0792cd
cee9f5
cfdfed
000000

Requirements
Must have
• Color like business card, Please, with the text under VaRLo, Correct address Benkelstr. 4 Zip code 9512 Seldorf, as well as Couvert Without addressing only design and logo with VaRlo
Nice to have
• more writing articles
Should not have
• Not too colored, Text under VaRLo, bright colors

```html
<!DOCTYPE html>
<html lang="en">
<head>
<meta charset="utf-8">
<title>Varlo Gmbh – Letterhead and Envelope</title>
<link href="https://fonts.googleapis.com/css2?family=Arimo:wght@700&family=Source+Sans+3:wght@400;600;700&display=swap" rel="stylesheet">
<style>
:root{
  --backdrop:#e0e0e0;
  --paper:#f6f6f6;
  --paper-white:#ffffff;
  --navy:#0555a3;
  --mid-blue:#3176b5;
  --pale-blue:#85abd2;
  --cyan:#34a7d8;
  --ink:#3a3a3a;
  --black:#000000;
}
*{margin:0;padding:0;box-sizing:border-box}
html,body{width:1200px;height:800px;overflow:hidden;background:var(--backdrop)}
body{position:relative;font-family:"Source Sans 3",sans-serif}

.letterhead{position:absolute;left:81px;top:69px;width:468px;height:661px;background:var(--paper);box-shadow:0 2px 8px rgba(0,0,0,.18);overflow:hidden}
.envelope{position:absolute;left:610px;top:298px;width:510px;height:428px}
.envelope-flap{position:absolute;left:0;top:0;width:510px;height:68px}
.envelope-body{position:absolute;left:0;top:67px;width:510px;height:361px;background:var(--paper-white);box-shadow:0 2px 8px rgba(0,0,0,.15);overflow:hidden}

.brand{position:absolute;display:flex;align-items:center;gap:6px}
.brand-mark{width:22px;height:22px;background:var(--navy)}
.brand-name{font-family:"Source Sans 3",sans-serif;font-weight:700;font-size:24px;color:var(--navy);letter-spacing:.5px;line-height:1}
.letterhead .brand{left:37px;top:34px}
.envelope-body .brand{left:27px;top:22px}

.greeting{position:absolute;left:36px;top:134px;font-family:"Arimo",sans-serif;font-weight:700;font-size:11.5px;color:var(--black)}
.letter-body{position:absolute;left:36px;top:161px;width:397px;font-size:10.2px;line-height:12.3px;color:var(--ink);text-align:justify}
.letter-body p{margin-bottom:12.3px}
.signature{position:absolute;left:42px;top:435px;width:80px;height:40px;background:linear-gradient(90deg,rgba(0,0,0,.07),rgba(0,0,0,.02))}

.wave{position:absolute;left:0;bottom:0;width:100%;display:block}
.contact{position:absolute;color:var(--paper-white);font-size:7.8px;line-height:12px}
.letterhead .contact{left:44px;bottom:19px}
.envelope-body .contact{left:35px;bottom:14px}
.contact-line{display:flex;align-items:center;gap:4px}
.contact-line svg{width:6px;height:6px;fill:var(--paper-white)}
</style>
</head>
<body>

<section class="letterhead">
  <div class="brand"><span class="brand-mark"></span><span class="brand-name">VaRLo</span></div>
  <p class="greeting">Dear Mr. Berno,</p>
  <div class="letter-body">
    <p>Lorem Ipsum is simply dummy text of the printing and typesetting industry. Lorem Ipsum has been the industry's standard dummy text ever since the 1500s, when an unknown printer took a galley of type and scrambled it to make a type specimen book. It has survived not only five centuries, but also the leap into electronic typesetting, remaining essentially unchanged.</p>
    <p>The standard chunk of Lorem Ipsum used since the 1500s is reproduced below for those interested. Sections 1.10.32 and 1.10.33 from "de Finibus Bonorum et Malorum" by Corvel are also reproduced in their exact original form, accompanied by English versions from the 1914 translation by H. Lenning</p>
    <p>Lorem Ipsum is simply dummy text of the printing and typesetting industry. Lorem Ipsum has been the industry's standard dummy text ever since the 1500s, when an unknown printer took a galley of type and scrambled it to make a type specimen book. It has survived not only five centuries, but also the leap into electronic typesetting, remaining essentially unchanged. It was popularised in the</p>
    <p>The standard chunk of Lorem Ipsum used since the 1500s is reproduced below for those interested. Sections 1.10.32 and 1.10.33 from "de Finibus Bonorum et Malorum" by Corvel are also reproduced in their exact original form, accompanied by English versions from the 1914 translation by H. Lenning</p>
  </div>
  <div class="signature" role="img" aria-label="Handwritten signature of the sender"></div>

  <svg class="wave" viewBox="0 0 585 90" preserveAspectRatio="none" height="72">
    <path d="M0,30 C150,-6 280,2 420,40 S560,26 585,4 L585,90 L0,90Z" fill="var(--pale-blue)"/>
    <path d="M0,34 C150,0 280,8 420,46 S560,32 585,9" fill="none" stroke="var(--paper-white)" stroke-width="2"/>
    <path d="M0,38 C150,4 280,12 420,52 S560,36 585,12 L585,90 L0,90Z" fill="var(--navy)"/>
    <path d="M0,44 C150,12 270,20 410,62 S555,44 585,16 L585,90 L0,90Z" fill="var(--cyan)"/>
  </svg>
  <div class="contact">
    <div>Benkelstr. 4 &nbsp;9512 Seldorf,</div>
    <div class="contact-line">
      <svg viewBox="0 0 10 10"><path d="M2,0 L4,3 L3,4 C4,6 5,7 6,7 L7,6 L10,8 L8,10 C4,10 0,6 0,2Z"/></svg>+41 71 555 02 38
      <svg viewBox="0 0 10 10"><rect x="0" y="2" width="10" height="7"/></svg>info@varlo.ch
      <svg viewBox="0 0 10 10"><circle cx="5" cy="5" r="5"/></svg>www.varlo.ch
    </div>
  </div>
</section>

<section class="envelope">
  <svg class="envelope-flap" viewBox="0 0 510 68" preserveAspectRatio="none">
    <path d="M0,68 L0,60 C2,50 8,47 20,44 C120,25 220,0 255,0 C290,0 390,25 490,44 C502,47 508,50 510,60 L510,68Z" fill="var(--pale-blue)"/>
  </svg>
  <div class="envelope-body">
    <div class="brand"><span class="brand-mark"></span><span class="brand-name">VaRLo</span></div>
    <svg class="wave" viewBox="0 0 637 90" preserveAspectRatio="none" height="72">
      <path d="M0,30 C160,-6 300,2 450,40 S610,26 637,2 L637,90 L0,90Z" fill="var(--pale-blue)"/>
      <path d="M0,34 C160,0 300,8 450,46 S610,32 637,7" fill="none" stroke="var(--paper-white)" stroke-width="2"/>
      <path d="M0,38 C160,4 300,12 450,52 S610,36 637,10 L637,90 L0,90Z" fill="var(--navy)"/>
      <path d="M0,44 C160,12 290,20 440,62 S605,44 637,14 L637,90 L0,90Z" fill="var(--cyan)"/>
    </svg>
    <div class="contact">
      <div>Benkelstr. 4 &nbsp;9512 Seldorf,</div>
      <div class="contact-line">
        <svg viewBox="0 0 10 10"><path d="M2,0 L4,3 L3,4 C4,6 5,7 6,7 L7,6 L10,8 L8,10 C4,10 0,6 0,2Z"/></svg>+41 71 555 02 38
        <svg viewBox="0 0 10 10"><rect x="0" y="2" width="10" height="7"/></svg>info@varlo.ch
        <svg viewBox="0 0 10 10"><circle cx="5" cy="5" r="5"/></svg>www.varlo.ch
      </div>
    </div>
  </div>
</section>

</body>
</html>
```